Luxury Resort Complex needs a Power Point Shell

Working in our primary color palate (pms colors can be provided and seen on our web site www.thewrenmere.com) design a title page, chapter page, and three slide page templates that include our logo either screened into the background or somewhere on the page which we can use for internal and external power point presentations.

Target Market(s)

Internal and External constituents

Industry/Entity Type

Hotel

```html
<!DOCTYPE html>
<html lang="en">
<head>
<meta charset="UTF-8">
<title>The Wrenmere – Your Private Golden Beach</title>
<link rel="stylesheet" href="https://fonts.googleapis.com/css2?family=Italiana&family=Montserrat:wght@400&display=swap">
<style>
  :root {
    --canvas: #f7f4ef;
    --ink: #1c1a1a;
    --gold: #d9b36a;
    --body-grey: #8a8580;
    --photo-top: #4a4248;
    --photo-bottom: #1e1a1d;
  }
  * { margin: 0; padding: 0; box-sizing: border-box; }
  html, body { width: 1200px; height: 675px; overflow: hidden; background: var(--canvas); }
  .slide { position: relative; width: 1200px; height: 675px; background: var(--canvas); }

  .title-bar {
    position: absolute; left: 19px; top: 16px; width: 1162px; height: 73px;
    background: var(--ink);
  }
  .title-bar__text {
    position: absolute; left: 24px; top: 14px;
    font-family: "Italiana", serif; font-weight: 400; font-size: 38px; letter-spacing: 1.6px;
    line-height: 44px; color: var(--gold); white-space: nowrap;
  }
  .title-bar__divider {
    position: absolute; left: 1050px; top: 12px; width: 1px; height: 52px; background: var(--gold);
  }
  .brand {
    position: absolute; left: 1062px; top: 0; width: 100px; height: 73px;
    display: flex; align-items: center; justify-content: center; text-align: center;
    font-family: "Italiana", serif; font-size: 13px; line-height: 16px; letter-spacing: 2px;
    color: var(--gold);
  }

  .frame { position: absolute; border: 1px solid var(--gold); }
  .frame--inner { left: 37px; top: 106px; width: 1127px; height: 554px; }
  .frame--outer { left: 19px; top: 120px; width: 1162px; height: 525px; }

  .kicker {
    position: absolute; left: 81px; top: 188px;
    font-family: "Montserrat", sans-serif; font-size: 18px; line-height: 22px; letter-spacing: 0.4px;
    color: var(--ink);
  }
  .heading {
    position: absolute; left: 81px; top: 218px;
    font-family: "Italiana", serif; font-weight: 400; font-size: 37px; line-height: 44px; letter-spacing: 1.2px;
    color: var(--ink); white-space: nowrap;
  }
  .heading-rule {
    position: absolute; left: 261px; top: 278px; width: 1px; height: 52px; background: var(--gold);
  }
  .body-copy {
    position: absolute; left: 81px; top: 351px;
    font-family: "Italiana", serif; font-size: 17px; line-height: 24px; letter-spacing: 0.5px;
    color: var(--body-grey); white-space: nowrap;
  }

  .photo {
    position: absolute; left: 624px; top: 153px; width: 494px; height: 449px;
    background: linear-gradient(180deg, var(--photo-top) 0%, var(--photo-bottom) 100%);
  }
</style>
</head>
<body>
<main class="slide">
  <header class="title-bar">
    <h1 class="title-bar__text">Where endless possibilities inspire the extraordinary</h1>
    <span class="title-bar__divider"></span>
    <div class="brand">THE<br>WRENMERE</div>
  </header>

  <div class="frame frame--inner"></div>
  <div class="frame frame--outer"></div>

  <section>
    <p class="kicker">REVEL IN BEACHFRONT BEAUTY</p>
    <h2 class="heading">Your Private Golden Beach</h2>
    <span class="heading-rule"></span>
    <p class="body-copy">Your backyard, a seemingly endless stretch<br>of private golden beach with the sun on your<br>face and the crashing waves as your rhythmic<br>backdrop. We invite you to make yourself<br>at home from sunrise to sunset with elegant<br>lounging, queen-size daybeds, gourmet<br>beachside bites, and a dedicated members-only<br>section.</p>
  </section>

  <div class="photo" role="img" aria-label="Photo: beach at sunset with palm trees"></div>
</main>
</body>
</html>
```